Change consultancy needs business card+ design

We need business card design for a Seattle based consulting firm called
Holloway + Brine. Our firm helps organizations shift their paradigms, lean into change, and reimagine the way they work together.
**Updated**
Our firm name is the logo using black and orange font, see attached. We would like to include the tagline "(Re)imagining how people work"
The final design should find a balance between playful, edgy and professional. For example, we are using the attached goldfish photo on our homepage and like the colors and concept of leaping forward. However, don't want to use the image on the card.
Lastly, depending on the winning design, we will also be looking for stationary/template design that will compliment the business card.
Industry/Entity Type
Business
Font styles to use
Other font styles liked:
- Helvetica
Look and feel
Each slider illustrates characteristics of the customer's brand and the style your logo design should communicate.

```html
<!DOCTYPE html>
<html lang="en">
<head>
<meta charset="utf-8">
<title>Holloway + Brine — Business Card</title>
<link rel="stylesheet" href="https://fonts.googleapis.com/css2?family=Arimo:wght@400;700&family=Jost:wght@300&display=swap">
<style>
  :root {
    --page: #ffffff;
    --card-edge: #9a9a9a;
    --brand-blue: #2f9fd5;
    --brand-orange: #f08a1c;
    --label-ink: #2d3a4a;
    --splash-light: #eaf5fb;
    --splash-mid: #b9dcee;
    --fish-orange: #f2893a;
    --back-tint: #d6ebf6;
  }
  * { margin: 0; padding: 0; box-sizing: border-box; }
  html, body {
    width: 1200px; height: 1000px; overflow: hidden;
    background: var(--page);
  }
  .sheet { position: relative; width: 1200px; height: 1000px; }

  .card {
    position: absolute;
    background: #fff;
    border: 1px solid var(--card-edge);
    overflow: hidden;
    font-family: "Arimo", "Helvetica Neue", Arial, sans-serif;
  }
  .card--front { left: 95px; top: 83px; width: 443px; height: 280px; }
  .card--back  { left: 672px; top: 80px; width: 447px; height: 283px;
    background: linear-gradient(90deg, var(--back-tint) 0%, #f4fafd 55%, #ffffff 100%); }

  .card__photo { position: absolute; }
  .card--front .card__photo {
    inset: 0;
    background:
      radial-gradient(ellipse 80px 38px at 340px 50px, var(--fish-orange) 0%, rgba(242,137,58,0.55) 55%, rgba(242,137,58,0) 100%),
      linear-gradient(35deg, var(--splash-light) 10%, var(--splash-mid) 38%, var(--splash-light) 62%, #ffffff 85%);
  }
  .card--back .card__photo {
    left: 170px; top: 0; right: 0; bottom: 0;
    background:
      radial-gradient(ellipse 40px 28px at 270px 25px, var(--fish-orange) 0%, rgba(242,137,58,0) 100%),
      radial-gradient(ellipse 120px 150px at 180px 150px, var(--splash-mid) 0%, rgba(185,220,238,0.4) 60%, rgba(255,255,255,0) 100%);
  }

  .brand {
    position: absolute; left: 37px; bottom: 24px;
    display: flex; align-items: baseline; white-space: nowrap;
  }
  .brand__name {
    font-weight: 700; font-size: 30px; letter-spacing: -0.3px;
    color: var(--brand-blue);
  }
  .brand__suffix {
    font-weight: 400; font-size: 23px;
    color: var(--brand-blue);
  }
  .brand__mark {
    width: 10px; height: 10px; margin-left: 8px;
    background: var(--brand-orange);
    align-self: center;
  }

  .contact-name {
    position: absolute; left: 22px; top: 21px;
    font-weight: 700; font-size: 19px; color: var(--brand-blue);
  }
  .contact-title {
    position: absolute; left: 22px; top: 44px;
    font-weight: 400; font-size: 14px; color: var(--brand-orange);
  }
  .contact-details {
    position: absolute; left: 29px; top: 197px;
    list-style: none; font-size: 12.5px; line-height: 18.5px;
    color: var(--brand-blue);
  }
  .contact-details .web { color: var(--brand-orange); }

  .side-label {
    position: absolute; top: 414px;
    font-family: "Jost", "Helvetica Neue", Arial, sans-serif;
    font-weight: 300; font-size: 17px; letter-spacing: 2.5px;
    color: var(--label-ink);
  }
  .side-label--front { left: 174px; }
  .side-label--back { left: 758px; }
</style>
</head>
<body>
<main class="sheet">
  <section class="card card--front" aria-label="Business card front">
    <div class="card__photo" role="img" aria-label="Photo of a goldfish leaping through a splash of water"></div>
    <div class="brand">
      <span class="brand__name">Holloway + Brine</span><span class="brand__suffix">, LLC</span>
      <span class="brand__mark" aria-hidden="true"></span>
    </div>
  </section>
  <p class="side-label side-label--front">FRONT</p>

  <section class="card card--back" aria-label="Business card back">
    <div class="card__photo" role="img" aria-label="Photo of a swirl of water droplets with a goldfish tail at the top edge"></div>
    <h1 class="contact-name">Nora Vance</h1>
    <p class="contact-title">Managing Partner</p>
    <ul class="contact-details">
      <li>Holloway + Brine, LLC</li>
      <li>206.555.0148</li>
      <li class="web">www.hollowaybrine.com</li>
    </ul>
  </section>
  <p class="side-label side-label--back">BACK</p>
</main>
</body>
</html>
```